DOUBLE SIDED BROCHURE NEEDED TO PROMOTE DOCTOR

I need a double sided DL size (99mm x 210mm) brochure, promoting a doctor seeing patients in a new area.

I want something professional. I have included the relevant information. I would also like the Dr's picture somwhere in the brochure, with a professional background. I wish to print these tomorrow, so i will pick a winner within 14 hours of posting this ad.

I have included an example of a brochures design that I recently saw, and its definietly a good starting point.

Medical

```html
<!DOCTYPE html>
<html lang="en">
<head>
<meta charset="utf-8">
<title>Dr. Elias Marwood – Referral Card</title>
<link rel="stylesheet" href="https://fonts.googleapis.com/css2?family=Lato:ital,wght@0,400;1,300;1,400;1,700&display=swap">
<style>
  :root {
    --stage: #e9e9ea;
    --slate: #8d8d8f;
    --navy: #25215e;
    --paper: #ffffff;
    --ink: #1a1a1a;
    --light: #ffffff;
    --photo-top: #6d6e73;
    --photo-bottom: #23242c;
  }
  * { box-sizing: border-box; margin: 0; padding: 0; }
  html, body { width: 1200px; height: 1073px; overflow: hidden; }
  body {
    background: var(--stage);
    font-family: "Lato", Arial, sans-serif;
    font-style: italic;
    position: relative;
  }
  .card {
    position: absolute;
    left: 100px;
    width: 1000px;
    height: 472px;
    background: var(--slate);
    overflow: hidden;
    box-shadow: 0 4px 14px rgba(0,0,0,.18);
  }
  .card--front { top: 46px; }
  .card--back { top: 556px; }

  .contact-band {
    position: absolute;
    left: 0; top: 279px;
    width: 800px; height: 92px;
    background: var(--navy);
    color: var(--light);
    font-size: 24px;
    line-height: 34px;
    padding: 13px 0 0 34px;
  }
  .referral-band {
    position: absolute;
    left: 0; top: 371px;
    width: 720px; height: 101px;
    background: var(--paper);
    color: var(--ink);
    font-size: 23px;
    padding: 36px 0 0 34px;
  }
  .portrait {
    position: absolute;
    right: 0; top: 28px;
    width: 290px; height: 444px;
    border-radius: 140px 140px 0 0;
    background: linear-gradient(180deg, var(--photo-top) 0%, #4a4b52 45%, var(--photo-bottom) 100%);
  }

  .greeting {
    position: absolute;
    left: 34px; top: 28px;
    color: var(--light);
    font-weight: 700;
    font-size: 55px;
    line-height: 60px;
  }
  .announcement {
    position: absolute;
    left: 34px; top: 96px;
    width: 660px;
    color: var(--light);
    font-weight: 400;
    font-size: 22px;
    line-height: 29px;
  }
  .announcement p + p { margin-top: 7px; }

  .intro {
    position: absolute;
    left: 34px; top: 42px;
    width: 680px;
    color: var(--light);
    font-size: 24px;
    line-height: 29px;
  }
  .services {
    position: absolute;
    left: 34px; top: 124px;
    width: 680px;
    display: flex;
    color: var(--light);
    font-size: 19px;
  }
  .services ul { list-style: none; }
  .services .col-left { width: 455px; }
  .services li {
    display: flex;
    align-items: flex-start;
    line-height: 22px;
    margin-bottom: 7px;
  }
  .services li svg { flex: none; width: 16px; height: 16px; margin: 3px 6px 0 0; }
  .services .note { display: block; font-size: 15px; line-height: 17px; }
</style>
</head>
<body>

<section class="card card--front">
  <h1 class="greeting">Dear Doctors,</h1>
  <div class="announcement">
    <p>We are pleased to announce that Dr. Elias Marwood is now consulting in Harbourvale, seeing public and private patients.</p>
    <p>Guaranteed appointment within two weeks, with patients having the option of surgery at Coastline Health Campus, Riverstone General Hospital or St. Clement's Private Hillcrest.</p>
  </div>
  <div class="contact-band">
    Harbourvale Clinic: 42 Wattlebrook Road, Harbourvale WA 6999.<br>
    Phone: 1300 555 014
  </div>
  <div class="referral-band">Please send all referrals by fax to (08) 5550 1472.</div>
  <div class="portrait" role="img" aria-label="Portrait photograph of Dr. Elias Marwood in a dark blazer and checked shirt"></div>
</section>

<section class="card card--back">
  <p class="intro">Dr. Marwood is a highly trained specialised surgeon, in all areas of Endocrine, Breast and General Surgery. Including:</p>
  <div class="services">
    <ul class="col-left">
      <li><svg viewBox="0 0 16 16"><circle cx="8" cy="8" r="8" fill="#fff"/><path d="M4.3 8.2l2.5 2.4 4.9-5" fill="none" stroke="#8d8d8f" stroke-width="2"/></svg>Thyroid Surgery</li>
      <li><svg viewBox="0 0 16 16"><circle cx="8" cy="8" r="8" fill="#fff"/><path d="M4.3 8.2l2.5 2.4 4.9-5" fill="none" stroke="#8d8d8f" stroke-width="2"/></svg><span>Parathyroid surgery<span class="note">(including minimally invasive parathyroidectomy)</span></span></li>
      <li><svg viewBox="0 0 16 16"><circle cx="8" cy="8" r="8" fill="#fff"/><path d="M4.3 8.2l2.5 2.4 4.9-5" fill="none" stroke="#8d8d8f" stroke-width="2"/></svg>Breast Cancer</li>
      <li><svg viewBox="0 0 16 16"><circle cx="8" cy="8" r="8" fill="#fff"/><path d="M4.3 8.2l2.5 2.4 4.9-5" fill="none" stroke="#8d8d8f" stroke-width="2"/></svg>Benign breast lesions</li>
    </ul>
    <ul class="col-right">
      <li><svg viewBox="0 0 16 16"><circle cx="8" cy="8" r="8" fill="#fff"/><path d="M4.3 8.2l2.5 2.4 4.9-5" fill="none" stroke="#8d8d8f" stroke-width="2"/></svg>Gallbladder surgery</li>
      <li><svg viewBox="0 0 16 16"><circle cx="8" cy="8" r="8" fill="#fff"/><path d="M4.3 8.2l2.5 2.4 4.9-5" fill="none" stroke="#8d8d8f" stroke-width="2"/></svg>Hernia surgery</li>
      <li><svg viewBox="0 0 16 16"><circle cx="8" cy="8" r="8" fill="#fff"/><path d="M4.3 8.2l2.5 2.4 4.9-5" fill="none" stroke="#8d8d8f" stroke-width="2"/></svg>Haemorrhoids</li>
      <li><svg viewBox="0 0 16 16"><circle cx="8" cy="8" r="8" fill="#fff"/><path d="M4.3 8.2l2.5 2.4 4.9-5" fill="none" stroke="#8d8d8f" stroke-width="2"/></svg>Carpal Tunnel</li>
      <li><svg viewBox="0 0 16 16"><circle cx="8" cy="8" r="8" fill="#fff"/><path d="M4.3 8.2l2.5 2.4 4.9-5" fill="none" stroke="#8d8d8f" stroke-width="2"/></svg>Vasectomy etc etc...</li>
    </ul>
  </div>
  <div class="contact-band">
    Harbourvale Clinic: 42 Wattlebrook Road, Harbourvale WA 6999.<br>
    Phone: 1300 555 014
  </div>
  <div class="referral-band">Please send all referrals by fax to (08) 5550 1472.</div>
  <div class="portrait" role="img" aria-label="Portrait photograph of Dr. Elias Marwood in a dark blazer and checked shirt"></div>
</section>

</body>
</html>
```